Visitenkarten-Design für Goldankauf und Verkauf von Trauringen
Zielgruppe
Goldankauf und Verkauf von Trauringen
Aufgabenstellung
Edel, nicht zu bunt, das Design soll sich dem Kunden einprägen, ansprechend, gerne können auch Wasserzeichen verwendet werden.

```html
<!DOCTYPE html>
<html lang="de">
<head>
<meta charset="utf-8">
<title>Aurelia – Visitenkarten</title>
<link rel="stylesheet" href="https://fonts.googleapis.com/css2?family=Cinzel:wght@400;500&family=Old+Standard+TT&display=swap">
<style>
  :root {
    --backdrop-inner: #ffffff;
    --backdrop-outer: #e9e9e9;
    --card-black: #050608;
    --gold-light: #fff59a;
    --gold-mid: #d8b85a;
    --gold-deep: #8a5a10;
    --gold-text: #e2c36a;
    --ink-white: #f4f1ea;
    --photo-warm: #6a3a22;
    --photo-violet: #3a2a44;
  }
  * { margin: 0; padding: 0; box-sizing: border-box; }
  html, body { width: 1200px; height: 1200px; overflow: hidden; }
  body {
    position: relative;
    background: radial-gradient(circle at 50% 50%, var(--backdrop-inner) 0%, var(--backdrop-outer) 90%);
    font-family: "Old Standard TT", Georgia, serif;
  }
  .card {
    position: absolute;
    left: 299px;
    width: 602px;
    height: 389px;
    background: var(--card-black);
    overflow: hidden;
  }
  .card--front { top: 197px; }
  .card--back { top: 620px; }
  .gold-band {
    position: absolute;
    left: 0; width: 100%; height: 11px;
    background: linear-gradient(90deg, var(--gold-light) 0%, var(--gold-mid) 55%, var(--gold-deep) 100%);
    z-index: 3;
  }
  .gold-band--top { top: 0; }
  .gold-band--bottom { bottom: 0; }

  /* front */
  .portrait-photo {
    position: absolute;
    left: 150px; top: 11px; right: 0; bottom: 11px;
    background:
      radial-gradient(ellipse at 82% 30%, #b98a78 0%, rgba(120,80,80,0.6) 22%, transparent 45%),
      radial-gradient(ellipse at 65% 85%, #a0702a 0%, rgba(110,60,20,0.6) 25%, transparent 55%),
      radial-gradient(ellipse at 95% 80%, var(--photo-warm) 0%, transparent 50%),
      linear-gradient(90deg, var(--card-black) 0%, #0a0608 30%, var(--photo-violet) 100%);
  }
  .brand {
    position: absolute;
    left: 25px; top: 148px;
    z-index: 2;
  }
  .brand__row { display: flex; align-items: center; gap: 12px; }
  .brand__mark {
    width: 30px; height: 30px;
    background: var(--gold-text);
  }
  .brand__name {
    font-family: "Cinzel", "Times New Roman", serif;
    font-weight: 400;
    font-size: 44px;
    line-height: 1;
    color: var(--gold-text);
    letter-spacing: 1px;
  }
  .brand__tagline {
    margin: 8px 0 0 42px;
    font-size: 15px;
    color: var(--ink-white);
    letter-spacing: 0.5px;
  }
  .front-url {
    position: absolute;
    left: 25px; top: 336px;
    font-family: "Cinzel", "Times New Roman", serif;
    font-size: 13.5px;
    color: var(--gold-text);
    letter-spacing: 0.4px;
    z-index: 2;
  }

  /* back */
  .jewellery-photo {
    position: absolute;
    left: 335px; top: 0; width: 267px; height: 310px;
    background:
      radial-gradient(ellipse at 45% 35%, #f0c84a 0%, #c99520 35%, rgba(120,80,10,0.7) 60%, transparent 78%),
      radial-gradient(ellipse at 80% 70%, #e8d8b0 0%, transparent 40%);
    z-index: 1;
  }
  .owner {
    position: absolute;
    left: 29px; top: 123px;
    font-family: "Cinzel", "Times New Roman", serif;
    font-size: 31px;
    line-height: 33px;
    color: var(--gold-text);
    z-index: 2;
  }
  .contact-line {
    position: absolute;
    left: 27px;
    display: flex; align-items: center;
    color: var(--ink-white);
    white-space: nowrap;
    z-index: 2;
  }
  .contact-line--primary { top: 200px; font-size: 15.5px; }
  .contact-line--small { font-size: 14px; }
  .contact-line--address { top: 298px; }
  .contact-line--web { top: 319px; }
  .contact-line--phone { top: 340px; }
  .icon { width: 14px; height: 16px; margin-right: 5px; flex: none; }
  .gap { margin-left: 7px; }
  .dot { margin: 0 6px; color: var(--gold-text); }
</style>
</head>
<body>
  <svg width="0" height="0" style="position:absolute">
    <defs>
      <linearGradient id="goldIcon" x1="0" y1="0" x2="1" y2="1">
        <stop offset="0" stop-color="#fff59a"/>
        <stop offset="1" stop-color="#b68a2a"/>
      </linearGradient>
    </defs>
  </svg>

  <section class="card card--front">
    <div class="gold-band gold-band--top"></div>
    <div class="portrait-photo" role="img" aria-label="Foto: Frau im Profil mit goldverzierten Lippen und goldener Spitze"></div>
    <div class="brand">
      <div class="brand__row">
        <span class="brand__mark"></span>
        <span class="brand__name">Aurelia</span>
      </div>
      <p class="brand__tagline">Goldankauf &amp; Trauringe</p>
    </div>
    <p class="front-url">WWW.AURELIA-HANAU.DE</p>
    <div class="gold-band gold-band--bottom"></div>
  </section>

  <section class="card card--back">
    <div class="gold-band gold-band--top"></div>
    <div class="jewellery-photo" role="img" aria-label="Foto: Haufen goldener Armreifen, Ringe und Perlenschmuck"></div>
    <h1 class="owner">INH. MARA<br>LINDQVIST</h1>

    <p class="contact-line contact-line--primary">
      <svg class="icon" viewBox="0 0 14 16"><path d="M3 1 L6 1 L6.5 4.5 L4.8 5.6 Q5.5 9.5 8 11.5 L9.5 10.2 L12 12.5 L11 15 Q5 15 2.5 8 Q1.5 4 3 1 Z" fill="url(#goldIcon)"/></svg>
      06181-7730410
      <svg class="icon gap" viewBox="0 0 16 14" style="width:18px"><rect x="0.5" y="2" width="15" height="10" fill="url(#goldIcon)"/><path d="M0.5 2 L8 8 L15.5 2" fill="none" stroke="#050608" stroke-width="1.2"/></svg>
      info@aurelia-hanau.de
    </p>

    <p class="contact-line contact-line--small contact-line--address">
      <svg class="icon" viewBox="0 0 14 16"><path d="M7 1 A5 5 0 0 1 12 6 Q12 9 7 15 Q2 9 2 6 A5 5 0 0 1 7 1 Z" fill="url(#goldIcon)"/><circle cx="7" cy="6" r="1.8" fill="#050608"/></svg>
      Lindenallee 12<span class="dot">•</span>63450 Hanau
    </p>
    <p class="contact-line contact-line--small contact-line--web">
      <svg class="icon" viewBox="0 0 14 14"><circle cx="7" cy="7" r="6" fill="none" stroke="url(#goldIcon)" stroke-width="1.3"/><ellipse cx="7" cy="7" rx="2.5" ry="6" fill="none" stroke="url(#goldIcon)" stroke-width="1"/><line x1="1" y1="7" x2="13" y2="7" stroke="url(#goldIcon)" stroke-width="1"/></svg>
      www.aurelia-hanau.de
      <svg class="icon gap" viewBox="0 0 16 14" style="width:17px"><rect x="0.5" y="2" width="15" height="10" fill="url(#goldIcon)"/><path d="M0.5 2 L8 8 L15.5 2" fill="none" stroke="#050608" stroke-width="1.2"/></svg>
      info@aurelia-hanau.de
    </p>
    <p class="contact-line contact-line--small contact-line--phone">
      <svg class="icon" viewBox="0 0 14 16"><path d="M3 1 L6 1 L6.5 4.5 L4.8 5.6 Q5.5 9.5 8 11.5 L9.5 10.2 L12 12.5 L11 15 Q5 15 2.5 8 Q1.5 4 3 1 Z" fill="url(#goldIcon)"/></svg>
      Tel.: 06181-7730410
      <svg class="icon gap" viewBox="0 0 18 16" style="width:19px"><rect x="0" y="5" width="3" height="10" fill="url(#goldIcon)"/><rect x="4" y="6" width="14" height="9" fill="url(#goldIcon)"/><rect x="7" y="1" width="8" height="5" fill="none" stroke="url(#goldIcon)" stroke-width="1.3"/></svg>
      Fax: 06181-7730411
    </p>
    <div class="gold-band gold-band--bottom"></div>
  </section>
</body>
</html>
```